Book cover design : The Copper Lantern

We need a striking book cover design for a book which will be published via Orvello Reader and as a paperback. The book is a simple short story - ghost story - for children. The book is set in a contemporary English town.

The title of the book is : The Copper Lantern
The author is: Walter Finch

The book is a story book, for children, aged approximately 11-15 years old.
It is a ghost story, but not too scary.

Text to go on the front cover:
The Copper Lantern

Walter Finch

Text to go on the back cover :

The Copper Lantern; a ghost story of controlled readability for students aged 11 to 15 years, (catch-up reading). Also for students of English as a foreign language.

Target Market(s)

A ghost story of controlled readability for students aged 11 to 15 years, (catch-up reading). Also for students of English as a foreign language.

```html
<!DOCTYPE html>
<html lang="en">
<head>
<meta charset="UTF-8">
<title>The Copper Lantern – Book Cover</title>
<link rel="stylesheet" href="https://fonts.googleapis.com/css2?family=Montserrat:wght@400;500&family=Pinyon+Script&display=swap">
<style>
  :root {
    --page-bg: #ffffff;
    --cover-black: #040506;
    --ink-white: #f7f7f5;
    --corridor-light: #f4efdc;
    --corridor-mist: #b9c6c9;
    --corridor-teal: #2c3d45;
    --corridor-deep: #0b1216;
  }
  * { box-sizing: border-box; margin: 0; padding: 0; }
  html, body {
    width: 720px;
    height: 1200px;
    overflow: hidden;
    background: var(--page-bg);
  }
  .canvas {
    position: relative;
    width: 720px;
    height: 1200px;
    display: flex;
    align-items: center;
    justify-content: center;
  }
  .book-cover {
    position: relative;
    width: 540px;
    height: 815px;
    background: var(--cover-black);
    overflow: hidden;
    box-shadow: 8px 14px 22px rgba(0, 0, 0, 0.28);
  }
  .cover-art {
    position: absolute;
    left: 0;
    top: 290px;
    width: 100%;
    height: 470px;
    background:
      radial-gradient(ellipse 22% 38% at 40% 72%, var(--corridor-light) 0%, rgba(244,239,220,0.6) 45%, rgba(244,239,220,0) 100%),
      radial-gradient(ellipse 55% 45% at 35% 70%, var(--corridor-mist) 0%, rgba(185,198,201,0.35) 50%, rgba(185,198,201,0) 100%),
      linear-gradient(90deg, var(--corridor-deep) 0%, var(--corridor-teal) 30%, #536d74 45%, var(--corridor-teal) 70%, var(--corridor-deep) 100%);
    -webkit-mask-image: linear-gradient(180deg, transparent 0%, #000 22%, #000 78%, transparent 100%);
    mask-image: linear-gradient(180deg, transparent 0%, #000 22%, #000 78%, transparent 100%);
  }
  .title {
    position: absolute;
    left: 0;
    right: 0;
    top: 52px;
    text-align: center;
    color: var(--ink-white);
  }
  .title-lead {
    display: block;
    font-family: "Montserrat", sans-serif;
    font-weight: 400;
    font-size: 52px;
    letter-spacing: 0.03em;
    line-height: 1;
  }
  .title-script {
    display: block;
    margin-top: 4px;
    font-family: "Pinyon Script", cursive;
    font-size: 118px;
    line-height: 1.1;
  }
  .author {
    position: absolute;
    left: 0;
    right: 0;
    bottom: 44px;
    text-align: center;
    font-family: "Montserrat", sans-serif;
    font-weight: 500;
    font-size: 33px;
    letter-spacing: 0.13em;
    color: var(--ink-white);
  }
</style>
</head>
<body>
  <main class="canvas">
    <section class="book-cover">
      <div class="cover-art" role="img" aria-label="Silhouette of a girl holding a teddy bear, walking down a dim school corridor toward bright light"></div>
      <h1 class="title">
        <span class="title-lead">THE COPPER</span>
        <span class="title-script">Lantern</span>
      </h1>
      <p class="author">WALTER FINCH</p>
    </section>
  </main>
</body>
</html>
```